Stationery Design Project

KT7 Staffing requires letterhead and business card designs for a company based in London. Just like the name, we're a management resourcing company, providing resources to third party companies. You can see www.kt7staffing-example.com for ideas on existing colour schemes and design concepts that have been implimented and agreed to. Ultimately the design should broadcast professionalism, safety and the concept of growth.

Target Market(s)

Financial institutes; friendly societies (All UK based)

Industry/Entity Type

Safety

Requirements
Must have
• Files produced should be print ready; and the text in them editable (eg address, name etc)

```html
<!DOCTYPE html>
<html lang="en">
<head>
<meta charset="utf-8">
<title>KT7 Staffing — Stationery</title>
<link rel="stylesheet" href="https://fonts.googleapis.com/css2?family=Questrial&display=swap">
<style>
  :root {
    --backdrop: #c3c3c3;
    --page: #ffffff;
    --teal: #1a9aa8;
    --sky: #7cbfdf;
    --ink: #2a2a2a;
    --mist-teal: rgba(26,154,168,0.16);
    --mist-sky: rgba(124,191,223,0.22);
    --shadow: 0 1px 4px rgba(0,0,0,0.35);
  }
  * { margin: 0; padding: 0; box-sizing: border-box; }
  html, body { width: 1200px; height: 843px; overflow: hidden; background: var(--page); }
  body { position: relative; font-family: "Questrial", "Century Gothic", sans-serif; color: var(--ink); }
  .backdrop { position: absolute; left: 0; top: 0; width: 1200px; height: 733px; background: var(--backdrop); }
  .sheet { position: absolute; background: var(--page); box-shadow: var(--shadow); overflow: hidden; }
  .card { border-radius: 9px; }
  .card-front { left: 204px; top: 62px; width: 231px; height: 129px; }
  .card-back { left: 206px; top: 211px; width: 231px; height: 129px; }
  .envelope { left: 31px; top: 395px; width: 585px; height: 255px; }
  .letterhead { left: 645px; top: 28px; width: 525px; height: 680px; }

  .wordmark { position: absolute; display: flex; align-items: center; gap: 6px; color: var(--teal); line-height: 1; white-space: nowrap; }
  .wordmark-dot { display: block; background: var(--sky); }
  .card-front .wordmark { left: 12px; top: 55px; font-size: 17px; }
  .card-back .wordmark { left: 86px; top: 20px; font-size: 16px; }
  .card .wordmark-dot { width: 12px; height: 12px; }
  .envelope .wordmark { left: 24px; top: 32px; font-size: 30px; gap: 10px; }
  .letterhead .wordmark { left: 24px; top: 34px; font-size: 32px; gap: 10px; }
  .envelope .wordmark-dot, .letterhead .wordmark-dot { width: 22px; height: 22px; }

  .accent { position: absolute; }
  .card-front .accent { left: 139px; top: 0; width: 92px; height: 129px;
    background: radial-gradient(ellipse 120% 90% at 100% 100%, var(--teal) 0%, rgba(26,154,168,0.85) 45%, rgba(124,191,223,0.6) 70%, rgba(124,191,223,0) 100%); }
  .envelope .accent { left: 480px; top: 120px; width: 105px; height: 135px;
    background: radial-gradient(ellipse 90% 80% at 80% 70%, var(--mist-teal) 0%, var(--mist-sky) 50%, rgba(124,191,223,0) 100%); }
  .letterhead .accent { left: 395px; top: 505px; width: 130px; height: 175px;
    background: radial-gradient(ellipse 90% 80% at 75% 65%, var(--mist-teal) 0%, var(--mist-sky) 50%, rgba(124,191,223,0) 100%); }

  .card-divider { position: absolute; left: 108px; top: 46px; width: 1px; height: 83px; background: var(--sky); }
  .holder { position: absolute; right: 129px; top: 74px; text-align: right; line-height: 1; }
  .holder-name { font-size: 8.5px; color: var(--ink); }
  .holder-role { font-size: 7.5px; color: var(--teal); margin-top: 1px; }
  .card-web { position: absolute; right: 129px; top: 105px; font-size: 6px; color: var(--teal); white-space: nowrap; }
  .contact { position: absolute; left: 113px; font-size: 6.4px; line-height: 9px; color: var(--ink); white-space: nowrap; }
  .contact-address { top: 70px; }
  .contact-direct { top: 96px; }
  .return-address { position: absolute; left: 64px; top: 214px; font-size: 10.5px; line-height: 11px; font-style: normal; }
  .letter-footer { position: absolute; left: 0; right: 0; top: 662px; text-align: center; font-size: 10.5px; }
</style>
</head>
<body>
  <div class="backdrop"></div>

  <section class="sheet card card-front">
    <div class="accent" role="img" aria-label="Decorative teal corner accent"></div>
    <span class="wordmark"><span class="wordmark-dot"></span>KT7 Staffing</span>
  </section>

  <section class="sheet card card-back">
    <span class="wordmark"><span class="wordmark-dot"></span>KT7 Staffing</span>
    <div class="card-divider"></div>
    <div class="holder">
      <div class="holder-name">Daniel Marsh</div>
      <div class="holder-role">manager</div>
    </div>
    <div class="card-web">www.kt7staffing-example.com</div>
    <div class="contact contact-address">City, State Name<br>12 Elm Row str.</div>
    <div class="contact contact-direct">555-014-7788<br>hello@kt7staffing-example.com</div>
  </section>

  <section class="sheet envelope">
    <div class="accent" role="img" aria-label="Faint decorative corner watermark"></div>
    <span class="wordmark"><span class="wordmark-dot"></span>KT7 Staffing</span>
    <address class="return-address">48 Harrow Lane , Suite 12<br>Brookfield, California 90210, USA</address>
  </section>

  <section class="sheet letterhead">
    <div class="accent" role="img" aria-label="Faint decorative corner watermark"></div>
    <span class="wordmark"><span class="wordmark-dot"></span>KT7 Staffing</span>
    <p class="letter-footer">48 Harrow Lane , Suite 12 • Brookfield, California 90210, USA • 555-010-2040</p>
  </section>
</body>
</html>
```